Website redesign for fast growing company looking to present a unique image

We're looking to revamp our online image to represent the professional, accomplished company we have become. We want to move beyond a templated look and feel to a custom design - we are eager to have you design a new public face for us! In particular, we need creative ways to display text to stand out. We are reaching top-level, C-suite executives and want to give them the confidence that we have the skills, talent, expertise, and knowledge to help their companies grow.
Updates

Designs look the same

Target Market(s)

contact centers, business process outsourcing

Industry/Entity Type

Call Center

Coding

Coded - Design and coding required

Number of Pages Required

4 page

Font styles to use
Sans Serif

Colors

Designer to choose colors to be used in the design.

Requirements
Must have
• Designed for a professional audience - C-suite executives - but that also shows our personality as a company that is nimble, personable, trustworthy, and smart. Must be lively, but not quirky. Professional, but not overly formal. Be bold with choices for imagery - we want to look unique so go beyond traditional "business/corporate" stock photos. Instead use imagery similar to what is on our staging website - torvenda.com/staging. Do not use the "neon" sign. Use colors to match and complement our logo - bright orange and dark blue. Creative text boxes that we can use throughout the site. I have attached pages of our current staging site to display some of the types of imagery that might work. We are looking for "professional with a personality" Note: this design will be transferred into a Wordpress framework.
Nice to have
• We like the animated text features of the Vorquin.com site - bold colors, great display of text features that break up the page and engage people to continue scrolling.
Should not have
• Cheesy stock photos of call center agents wearing headsets. Overly used stock photos of professionals in suits shaking hands, high-rise buildings, connection/network graphics. Current management does not like the neon sign graphics displayed on our staging site (torvenda.com/staging). We do not like style of sites that use cartoon-like icons and figures.

```html
<!DOCTYPE html>
<html lang="en">
<head>
<meta charset="utf-8">
<title>Torvenda — Contact Center Experts</title>
<link href="https://fonts.googleapis.com/css2?family=Poppins:wght@400;500;600;700&family=Open+Sans:wght@400;600;700&display=swap" rel="stylesheet">
<style>
:root{
  --stage:#eef1f5;
  --blue:#1d5aa8;
  --blue-deep:#0b4ea2;
  --orange:#ee5a2f;
  --coral:#e8573a;
  --navy:#2c3a5e;
  --ink:#1b2440;
  --text:#555b66;
  --muted:#8a8f98;
  --white:#ffffff;
  --footer:#16181c;
  --footer-text:#c8cbd0;
  --line:#e6e8ec;
}
*{box-sizing:border-box;margin:0;padding:0}
html,body{width:1200px;height:1200px;overflow:hidden;background:var(--stage)}
body{font-family:"Open Sans",Arial,sans-serif;color:var(--text)}
.page{position:absolute;left:350px;top:14px;width:500px;height:1172px;background:var(--white);overflow:hidden}
.abs{position:absolute}
.photo{position:absolute}
.heading{font-family:"Poppins",Arial,sans-serif}

/* hero */
.hero{left:0;top:0;width:500px;height:195px;background:linear-gradient(135deg,#2a6bbd 0%,#1d5aa8 55%,#174c92 100%)}
.hero-eyebrow{left:0;top:38px;width:500px;text-align:center;font-size:4px;font-weight:700;letter-spacing:.4px;color:var(--white)}
.hero-title{left:0;top:46px;width:500px;text-align:center;font-size:19px;line-height:21px;font-weight:600;color:var(--white)}
.hero-sub{left:0;top:95px;width:500px;text-align:center;font-size:4.3px;color:var(--white)}
.btn{position:absolute;background:var(--orange);color:var(--white);font-size:4px;font-weight:600;text-align:center;border-radius:2px}
.hero-btn{left:227px;top:110px;width:46px;height:11px;line-height:11px}

/* feature cards */
.feature-card{position:absolute;top:170px;width:93px;height:102px;padding:10px 8px;text-align:center}
.feature-card h3{font-family:"Poppins",Arial,sans-serif;font-size:6px;line-height:7px;font-weight:500;margin-bottom:5px}
.feature-card p{font-size:3.2px;line-height:4.4px}
.feature-card .more{position:absolute;left:0;bottom:10px;width:100%;font-size:3.4px;font-weight:600}
.card-light{left:110px;background:var(--white);box-shadow:0 2px 6px rgba(0,0,0,.12);color:var(--text)}
.card-light h3{color:var(--ink)}
.card-light .more{color:var(--orange)}
.card-orange{left:203px;background:var(--coral);color:var(--white)}
.card-navy{left:296px;background:var(--navy);color:var(--white)}

/* new world */
.world-title{left:113px;top:297px;font-size:6.2px;font-weight:700;color:var(--ink)}
.world-copy{left:113px;top:306px;width:170px;font-size:3.6px;line-height:5px}
.checklist{left:113px;top:338px;list-style:none;font-size:3.8px;line-height:7px;color:var(--ink)}
.checklist li::before{content:"✓";color:var(--orange);margin-right:3px}
.world-btn{left:113px;top:378px;width:42px;height:9px;line-height:9px}
.world-photo{left:299px;top:299px;width:88px;height:116px;background:linear-gradient(160deg,#d9d4cc,#8e8a84 60%,#5a5652)}

/* hiring */
.rule{left:0;width:500px;height:1px;background:var(--line)}
.hiring-title{left:113px;top:440px;font-size:8.5px;font-weight:700;color:var(--ink)}
.hiring-title span{color:var(--orange)}
.hiring-copy{left:113px;top:452px;width:215px;font-size:3.3px;line-height:4.6px}
.hiring-btn{left:338px;top:446px;width:48px;height:11px;line-height:11px;border-radius:6px}
.section-shadow{left:0;top:495px;width:500px;height:6px;background:linear-gradient(var(--line),transparent)}

/* services */
.services-title{left:0;top:532px;width:500px;text-align:center;font-size:11px;font-weight:500;color:var(--ink)}
.services-sub{left:0;top:552px;width:500px;text-align:center;font-size:4px}
.service-grid{left:133px;top:577px;width:235px;height:230px}
.svc-title{position:absolute;text-align:center;font-family:"Poppins",Arial,sans-serif;font-size:4px;line-height:4.6px;font-weight:600;color:var(--ink)}
.svc-copy{position:absolute;text-align:center;font-size:3px;line-height:4px;color:var(--muted)}
.svc-more{position:absolute;text-align:center;font-size:3px;color:var(--orange);font-weight:600}

/* cloud */
.cloud{left:0;top:820px;width:500px;height:135px;background:var(--blue-deep)}
.cloud-shadow{left:112px;top:854px;width:78px;height:70px;background:#2f5f9e}
.cloud-photo{left:108px;top:850px;width:78px;height:70px;background:linear-gradient(135deg,#e6ddd3,#a89a8d 55%,#4a4340)}
.cloud-title{left:210px;top:858px;font-size:14px;font-weight:500;color:var(--white)}
.cloud-copy{left:205px;top:883px;width:200px;text-align:center;font-size:4.2px;line-height:6px;color:var(--white)}

/* help */
.help-title{left:110px;top:975px;width:120px;font-size:11px;line-height:11.5px;font-weight:500;color:var(--ink)}
.help-copy{left:110px;top:1014px;width:115px;font-size:4.6px;line-height:6px;color:var(--ink)}
.help-btn{left:110px;top:1038px;width:46px;height:11px;line-height:11px;font-size:6px;font-family:"Poppins",Arial,sans-serif;letter-spacing:.6px}
.help-photo{left:300px;top:1010px;width:94px;height:53px;background:linear-gradient(120deg,#3a4656,#8c96a3 55%,#2a2f37);border-radius:2px}

/* footer */
.footer{left:0;top:1077px;width:500px;height:95px;background:var(--footer)}
.foot-head{position:absolute;font-size:3.4px;font-weight:700;color:var(--white);letter-spacing:.2px}
.foot-list{position:absolute;list-style:none;font-size:3.2px;line-height:5.6px;color:var(--footer-text)}
.foot-list li{display:flex;align-items:center;gap:3px}
.dot{display:inline-block;width:3.4px;height:3.4px;border-radius:50%;background:var(--orange);flex:none}
.brand{position:absolute;font-family:"Poppins",Arial,sans-serif;font-size:7px;font-weight:600;color:var(--white)}
.brand-faint{color:#5c6068}
.brand-tag{position:absolute;font-size:3px;color:var(--footer-text)}
</style>
</head>
<body>
<main class="page">

  <section class="hero abs" role="img" aria-label="Photo of a desk with a coffee cup and keyboard under a blue overlay"></section>
  <p class="hero-eyebrow abs">CONTACT CENTER EXPERTS</p>
  <h1 class="hero-title abs heading">Get More From Your<br>Customer Interactions</h1>
  <p class="hero-sub abs">Lift Your Top and Bottom Lines with Professional Outsourcing Solutions From Torvenda</p>
  <a class="btn hero-btn">Contact Us</a>

  <article class="feature-card card-light">
    <h3>Meet Your Customer<br>Service Goals</h3>
    <p>Our custom contact center solutions support your customers, grow retention and help your team manage peaks and daily work, keeping every interaction friendly and fast.</p>
    <span class="more">Learn More ›</span>
  </article>
  <article class="feature-card card-orange">
    <h3>Gain Insight and<br>Scalability</h3>
    <p>Learn insights from every interaction and scale your teams up or down as demand changes, with reporting that keeps leaders informed on results and next steps.</p>
    <span class="more">Learn More ›</span>
  </article>
  <article class="feature-card card-navy">
    <h3>Join Our Team</h3>
    <p>We're growing fast and looking for passionate professionals to join our team. Learn more about our culture, benefits and the roles we have open right now.</p>
    <span class="more">Learn More ›</span>
  </article>

  <h2 class="world-title abs heading">IT'S A NEW WORLD. ARE YOU READY?</h2>
  <p class="world-copy abs">It's time to find solutions that deliver more value. Shed the human interactions that cost you money and deliver your full value. Get more by partnering with Torvenda for Customer Service, Tech Support, and Business Process Outsourcing solutions.</p>
  <ul class="checklist abs">
    <li>More Value</li>
    <li>More Performance</li>
    <li>More Agility</li>
    <li>More Insights</li>
    <li>More Options</li>
  </ul>
  <a class="btn world-btn">Read More</a>
  <div class="photo world-photo" role="img" aria-label="Photo of a bright office interior with tall windows"></div>

  <div class="rule abs" style="top:425px"></div>
  <h2 class="hiring-title abs heading">We're <span>Hiring!</span></h2>
  <p class="hiring-copy abs">Are you ready for a career path you are passionate about? Our team works hard and has fun while doing it. We offer competitive pay, growth paths and a friendly culture for people who enjoy helping customers every day and want to build a future with us.</p>
  <a class="btn hiring-btn">Learn more</a>
  <div class="section-shadow abs"></div>

  <h2 class="services-title abs heading">Services We Offer</h2>
  <p class="services-sub abs">Flexible, versatile, end-to-end outsourcing options to help you get more of what your business needs.</p>

  <section class="service-grid abs">
    <div class="photo" style="left:0;top:0;width:105px;height:79px;background:linear-gradient(135deg,#3c4250,#8f95a0 50%,#dfe2e6)" role="img" aria-label="Photo of hands reviewing printed charts"></div>
    <div class="photo" style="left:109px;top:0;width:50px;height:38px;background:linear-gradient(135deg,#e8e6e3,#b7b1aa)" role="img" aria-label="Photo of a team at a desk seen from above"></div>
    <div class="photo" style="left:164px;top:0;width:51px;height:38px;background:linear-gradient(135deg,#eef0f2,#9aa2ac)" role="img" aria-label="Photo of a person working at a laptop"></div>

    <p class="svc-title" style="left:105px;top:48px;width:58px">Government Contact<br>Center Solutions</p>
    <p class="svc-copy" style="left:107px;top:59px;width:54px">You can concentrate more time on the most successful aspects of your company.</p>
    <p class="svc-more" style="left:107px;top:82px;width:54px">Learn More ›</p>

    <p class="svc-title" style="left:160px;top:48px;width:58px">Customer Service for<br>Ecommerce</p>
    <p class="svc-copy" style="left:162px;top:59px;width:54px">You can concentrate more time on the most successful aspects of your company.</p>
    <p class="svc-more" style="left:162px;top:82px;width:54px">Learn More ›</p>

    <p class="svc-title" style="left:0;top:90px;width:105px">Insurance Contact Center Services</p>
    <p class="svc-copy" style="left:0;top:96px;width:105px">You can concentrate more time on the most successful aspects of your company.</p>

    <div class="photo" style="left:0;top:108px;width:51px;height:37px;background:linear-gradient(135deg,#c9c6c2,#6f6a66)" role="img" aria-label="Photo of a desk with a keyboard and notebook"></div>
    <div class="photo" style="left:54px;top:108px;width:51px;height:34px;background:linear-gradient(135deg,#a48d7c,#5d4c43)" role="img" aria-label="Photo of a laptop on a wooden table"></div>
    <div class="photo" style="left:109px;top:96px;width:113px;height:71px;background:linear-gradient(135deg,#e9eaec,#a7adb5 55%,#4d5561)" role="img" aria-label="Photo of a man working at a computer in an office"></div>

    <p class="svc-title" style="left:-4px;top:156px;width:59px">Tech Support Contact<br>Center Solutions</p>
    <p class="svc-copy" style="left:0;top:167px;width:51px">You can concentrate more time on the most successful aspects of your company.</p>
    <p class="svc-more" style="left:0;top:192px;width:51px">Learn More ›</p>

    <p class="svc-title" style="left:50px;top:153px;width:59px">Business Process<br>Outsourcing Solutions</p>
    <p class="svc-copy" style="left:54px;top:164px;width:51px">You can concentrate more time on the most successful aspects of your company.</p>
    <p class="svc-more" style="left:54px;top:188px;width:51px">Learn More ›</p>

    <p class="svc-title" style="left:109px;top:177px;width:113px">Commercial Business Customer Service<br>and Tech Support</p>
    <p class="svc-copy" style="left:109px;top:189px;width:113px">You can concentrate more time on the most successful aspects of your company.</p>
    <p class="svc-more" style="left:109px;top:208px;width:113px">Learn More ›</p>
  </section>

  <section class="cloud abs"></section>
  <div class="cloud-shadow abs"></div>
  <div class="photo cloud-photo" role="img" aria-label="Photo of a woman working on a laptop"></div>
  <h2 class="cloud-title abs heading">We Leverage the Cloud</h2>
  <p class="cloud-copy abs">Lorem ipsum dolor sit amet, consectetur adipiscing elit. Ut elit tellus, luctus nec ullamcorper mattis, pulvinar dapibus leo. Lorem ipsum dolor sit amet, consectetur adipiscing elit. Ut elit tellus, luctus nec ullamcorper mattis, pulvinar dapibus leo.</p>

  <h2 class="help-title abs heading">We help your time and work for your money.</h2>
  <p class="help-copy abs">We deliver true results, focusing on strategic decisions and practical actions tailored to our clients' unique reality.</p>
  <a class="btn help-btn">Hire Us</a>
  <div class="photo help-photo" role="img" aria-label="Photo of two colleagues working together at laptops"></div>

  <footer class="footer abs">
    <p class="foot-head" style="left:128px;top:14px">ADDRESS LIST</p>
    <ul class="foot-list" style="left:128px;top:20px;width:60px">
      <li><span class="dot"></span>18 Calder Lane Unit 4, Suite</li>
      <li style="padding-left:6px">210 Ashford, ME 04890</li>
      <li><span class="dot"></span>+1 207.555.0148</li>
      <li><span class="dot"></span>18 Calder Lane Unit 4, Suite</li>
      <li style="padding-left:6px">210 Ashford, ME 04890</li>
      <li><span class="dot"></span>+1 207.555.0148</li>
      <li><span class="dot"></span>info@torvenda.com</li>
    </ul>

    <p class="foot-head" style="left:193px;top:14px">SOCIAL NETWORKS</p>
    <ul class="foot-list" style="left:193px;top:20px">
      <li><span class="dot"></span>Torvenda</li>
      <li><span class="dot"></span>@Torvenda</li>
      <li><span class="dot"></span>Torvenda</li>
      <li><span class="dot"></span>Torvenda</li>
      <li><span class="dot"></span>@Torvenda</li>
      <li><span class="dot"></span>Torvenda</li>
      <li><span class="dot"></span>Torvenda</li>
    </ul>

    <p class="foot-head" style="left:256px;top:14px">LINKS LIST</p>
    <ul class="foot-list" style="left:256px;top:20px">
      <li>Home</li><li>About Us</li><li>Service</li><li>Home</li><li>About Us</li><li>Service</li><li>Contact</li>
    </ul>

    <p class="brand" style="left:320px;top:12px">Torvenda LLC.</p>
    <p class="brand-tag" style="left:320px;top:23px">Contact Center</p>
    <p class="brand brand-faint" style="left:320px;top:34px;font-size:5px">Torvenda LLC.</p>
    <p class="brand-tag" style="left:320px;top:42px">Contact Center</p>
  </footer>

</main>
</body>
</html>
```